"Tidewell Fellowship" needs a logo design that represents a Christian family boating ministry

Mission Statement:
“Providing compassion, care and opportunities to create memories for marginalized groups of society through ocean therapy.”
Bible verse:
Colossians 3:12 – “Therefore, as God’s chosen people, holy and dearly loved, clothe yourselves with compassion, kindness, humility, gentleness and patience.”
Target Market(s)
HOMELESS (who have gone through shelters and are on the road to recovery)
CHURCH GROUPS
INJURED MILITARY VETERANS
YOUTH AT RISK (orphans, human trafficking survivors)
SICKLY (hospitalized who can get out once in a while)
CAREGIVERS (single moms, military spouses caring for injured vets, families of those in prison)
ELDERLY (retirement centers)
SMALL BUSINESS STAFF OUTINGS
SPECIAL EVENTS
Industry/Entity Type
Ministry
Contact Information for Business Card
Captain Glen Marlowe @ 808-491-3027
Priscilla Marlowe @ 808-493-5184
info@tidewellfellowship.example
www.tidewellfellowship.example (not active yet but hopefully, soon)
Requirements
Must have
- Catch-phrase words maybe for back of business card:
- "Tide-Bound --- Kindness --- Making moments out at sea"
Nice to have
- Added 2 photo files just for visuals:
- 1 photo is of our boat.
- Other photo is our daughter's artwork on a cooler she made (for father's day gift)...might be nice and fun to incorporate daughter's artwork/inspiration into logo...but not sure if it looks to busy

```html
<!DOCTYPE html>
<html lang="en">
<head>
<meta charset="utf-8">
<title>Tidewell Fellowship – Business Card</title>
<link href="https://fonts.googleapis.com/css2?family=Open+Sans:wght@400;600;700&display=swap" rel="stylesheet">
<style>
  :root {
    --page-bg: #ece9e4;
    --card-white: #ffffff;
    --ministry-blue: #1b5aa8;
    --navy: #2a3f5f;
    --swoosh-red: #e3202a;
    --text-dark: #333a44;
    --verse-text: #dbe6f5;
    --photo-top: #8f9aa6;
    --photo-mid: #b9c2cc;
    --photo-low: #9aa5b1;
  }
  * { box-sizing: border-box; margin: 0; padding: 0; }
  html, body {
    width: 1200px; height: 900px; overflow: hidden;
    background: var(--page-bg);
    font-family: "Open Sans", Arial, sans-serif;
  }
  .card-set {
    position: absolute; inset: 0;
    display: flex; align-items: center; justify-content: center; gap: 40px;
  }
  .card {
    position: relative; width: 540px; height: 309px; overflow: hidden;
    background: var(--card-white);
    box-shadow: 0 6px 18px rgba(0,0,0,0.18);
  }

  /* Back of card */
  .card-back .boat-photo {
    position: absolute; inset: 0;
    background: linear-gradient(160deg, var(--photo-top) 0%, var(--photo-mid) 45%, var(--photo-low) 100%);
  }
  .card-back .catch-phrase {
    position: absolute; left: 28px; bottom: 34px;
    color: #fff; font-weight: 600; font-size: 14px; letter-spacing: 0.2px;
    text-shadow: 0 1px 2px rgba(0,0,0,0.35);
  }
  .catch-phrase .divider { margin: 0 6px; }

  /* Front of card */
  .card-front .wave { position: absolute; inset: 0; width: 100%; height: 100%; }
  .contacts { position: absolute; left: 40px; top: 44px; }
  .person-name {
    color: var(--ministry-blue); font-weight: 700; font-size: 19px;
    text-transform: uppercase; line-height: 1.1;
  }
  .phone-line, .web-line {
    display: flex; align-items: center; gap: 7px;
    color: var(--text-dark); font-size: 14.5px; line-height: 1.3;
  }
  .phone-line { margin-bottom: 14px; }
  .web-list { margin-top: 10px; }
  .icon { width: 12px; height: 12px; flex: none; }
  .brand {
    position: absolute; right: 38px; top: 88px;
    display: flex; align-items: center; gap: 8px;
  }
  .brand-dot { width: 14px; height: 14px; border-radius: 50%; background: var(--ministry-blue); }
  .brand-name { color: var(--navy); font-weight: 600; font-size: 21px; }
  .verse {
    position: absolute; right: 26px; bottom: 18px; width: 400px;
    color: var(--verse-text); font-size: 11px; line-height: 1.45; text-align: right;
  }
</style>
</head>
<body>
<main class="card-set">

  <section class="card card-back">
    <div class="boat-photo" role="img" aria-label="Photograph of the ministry's white sport-fishing boat moored on calm water"></div>
    <p class="catch-phrase">Tide-Bound<span class="divider">|</span>Kindness<span class="divider">|</span>Making moments out at sea</p>
  </section>

  <section class="card card-front">
    <svg class="wave" viewBox="0 0 540 309" preserveAspectRatio="none" aria-hidden="true">
      <path fill="var(--ministry-blue)" d="M0 262 C 150 232, 290 205, 390 178 C 460 160, 505 152, 540 150 L540 309 L0 309 Z"/>
      <path fill="var(--swoosh-red)" d="M0 236 C 120 214, 250 196, 340 172 C 270 200, 140 225, 0 252 Z"/>
    </svg>

    <div class="contacts">
      <h2 class="person-name">Captain Glen Marlowe</h2>
      <p class="phone-line">
        <svg class="icon" viewBox="0 0 24 24"><path fill="var(--swoosh-red)" d="M6.6 10.8a15 15 0 0 0 6.6 6.6l2.2-2.2a1 1 0 0 1 1-.25 11.4 11.4 0 0 0 3.6.57 1 1 0 0 1 1 1V20a1 1 0 0 1-1 1A17 17 0 0 1 3 4a1 1 0 0 1 1-1h3.5a1 1 0 0 1 1 1c0 1.25.2 2.45.57 3.6a1 1 0 0 1-.25 1z"/></svg>
        808-491-3027
      </p>
      <h2 class="person-name">Priscilla Marlowe</h2>
      <p class="phone-line">
        <svg class="icon" viewBox="0 0 24 24"><path fill="var(--swoosh-red)" d="M6.6 10.8a15 15 0 0 0 6.6 6.6l2.2-2.2a1 1 0 0 1 1-.25 11.4 11.4 0 0 0 3.6.57 1 1 0 0 1 1 1V20a1 1 0 0 1-1 1A17 17 0 0 1 3 4a1 1 0 0 1 1-1h3.5a1 1 0 0 1 1 1c0 1.25.2 2.45.57 3.6a1 1 0 0 1-.25 1z"/></svg>
        808-493-5184
      </p>
      <div class="web-list">
        <p class="web-line">
          <svg class="icon" viewBox="0 0 24 24"><rect x="2" y="5" width="20" height="14" rx="1" fill="var(--ministry-blue)"/><path d="M3 6l9 7 9-7" stroke="#fff" stroke-width="1.8" fill="none"/></svg>
          info@tidewellfellowship.example
        </p>
        <p class="web-line">
          <svg class="icon" viewBox="0 0 24 24"><circle cx="12" cy="12" r="10" fill="var(--ministry-blue)"/><path d="M2 12h20M12 2c3 3 3 17 0 20M12 2c-3 3-3 17 0 20" stroke="#fff" stroke-width="1.4" fill="none"/></svg>
          www.tidewellfellowship.example
        </p>
      </div>
    </div>

    <div class="brand">
      <span class="brand-dot"></span>
      <span class="brand-name">Tidewell Fellowship</span>
    </div>

    <p class="verse">Therefore, as God's chosen people, holy and dearly loved, clothe yourselves with compassion, kindness, humility, gentleness and patience. - Colossians 3:12</p>
  </section>

</main>
</body>
</html>
```